Medigap Insurance Interactive website

We are looking at redesigning our website for a more up to date and responsive look and feel. We will code this site using Bootstrap 3 so please research and know how to design for this. Attached is our logo and a wireframe for the new site.
I look forward to seeing what you guys can do.

Target Market(s)

People elegible for Medigap Insurance in the US

Industry/Entity Type

Insurance

Number of Pages Required

5+ page

Font styles to use
Sans Serif

Requirements
Must have
• Match the logo
• Be Bootstrap 3 compatible design
• Font Awesome Icons

```html
<!DOCTYPE html>
<html lang="en">
<head>
<meta charset="utf-8">
<title>Gapwise360 – Medicare Supplement</title>
<link rel="stylesheet" href="https://fonts.googleapis.com/css2?family=Merriweather:wght@400;700;900&family=Roboto:wght@400;500&display=swap">
<style>
:root{
  --navy:#0d3a72;
  --navy-2:#1a4478;
  --navy-3:#2b5186;
  --navy-4:#3e6196;
  --red:#b8201e;
  --ink:#333;
  --muted:#555;
  --line:#dcdcdc;
  --grey-bg:#e8e8e8;
  --footer:#2e2e2e;
}
*{margin:0;padding:0;box-sizing:border-box}
html,body{width:1200px;height:952px;overflow:hidden;background:#fff}
body{font-family:"Roboto",sans-serif;color:var(--ink);position:relative}
.serif{font-family:"Merriweather",serif}

/* header */
.site-header{position:absolute;left:0;top:0;width:1200px;height:80px;background:#fff}
.brand{position:absolute;left:22px;top:25px;font-family:"Merriweather",serif;font-size:19px;font-weight:400;color:var(--red);letter-spacing:-.2px}
.nav{position:absolute;top:22px;left:193px;display:flex;align-items:center;height:33px}
.nav a{font-family:"Merriweather",serif;font-size:12px;color:#444;text-decoration:none;white-space:nowrap}
.nav .active{background:var(--navy);color:#fff;font-weight:700;padding:0 11px;height:33px;line-height:33px}
.nav-item{position:absolute;top:31px;font-family:"Merriweather",serif;font-size:12px;color:#444}
.divider{position:absolute;top:0;width:1px;height:80px;background:var(--line)}
.rates{position:absolute;left:902px;top:18px}
.rates .label{font-family:"Merriweather",serif;font-size:11px;color:#555}
.rates .phone{font-family:"Merriweather",serif;font-size:18px;color:var(--red);margin-top:3px}
.connect{position:absolute;left:1077px;top:18px}
.connect .label{font-family:"Merriweather",serif;font-size:11px;color:#555}
.socials{display:flex;gap:7px;margin-top:7px}
.socials span{width:20px;height:20px;border-radius:50%;display:block}

/* hero */
.hero-photo{position:absolute;left:0;top:80px;width:742px;height:419px;background:linear-gradient(100deg,#c9d6df 0%,#e3eaee 35%,#b7c1c8 60%,#8f9aa4 100%)}
.why-box{position:absolute;left:77px;top:269px;width:337px;height:133px;background:rgba(50,50,50,.78);padding:20px 22px}
.why-box h1{font-family:"Merriweather",serif;font-weight:900;font-size:36px;color:#fff;line-height:1;margin-bottom:13px}
.why-box p{font-size:12.5px;color:#fff;line-height:18px}
.hero-video{position:absolute;left:742px;top:80px;width:458px;height:419px;background:linear-gradient(160deg,#6b5f52 0%,#b7b8bd 45%,#dfe2e6 100%)}
.play{position:absolute;left:183px;top:160px}
.video-bar{position:absolute;left:0;bottom:0;width:458px;height:27px;background:#1e1e1e;color:#ddd;font-size:11px}
.video-bar .progress{position:absolute;left:0;top:-3px;width:458px;height:3px;background:#666}
.video-bar .progress i{display:block;width:174px;height:3px;background:#eee}
.video-bar .time{position:absolute;left:255px;top:7px}

/* feature bar */
.features{position:absolute;left:0;top:499px;width:1200px;height:79px;display:flex}
.feature{height:79px;display:flex;align-items:center;justify-content:center;gap:14px;color:#fff;font-family:"Merriweather",serif;font-size:16px}
.feature b{font-weight:900}
.f1{width:302px;background:var(--navy)}
.f2{width:303px;background:var(--navy-2)}
.f3{width:304px;background:var(--navy-3)}
.f4{width:291px;background:var(--navy-4)}

/* content */
.content{position:absolute;left:0;top:578px;width:1200px;height:308px;display:flex}
.col{height:308px;position:relative;text-align:center}
.col-welcome{width:398px;background:linear-gradient(180deg,#f7f7f7,#fff)}
.col-testimonial{width:400px;background:linear-gradient(180deg,#e4e4e4,#eeeeee)}
.col-updates{width:402px;background:linear-gradient(180deg,#f7f7f7,#fff)}
.kicker{position:absolute;top:24px;left:0;width:100%;font-family:"Merriweather",serif;font-size:11px;color:var(--red)}
.col h2{position:absolute;top:40px;left:0;width:100%;font-family:"Merriweather",serif;font-weight:400;font-size:19px;color:var(--navy)}
.col h2 b{font-weight:900}
.col-testimonial h2,.col-updates h2{top:36px}
.rule{position:absolute;top:71px;left:50%;margin-left:-37px;width:74px;height:2px;background:var(--navy)}
.col .copy{position:absolute;left:36px;right:36px;top:101px;font-size:11.5px;line-height:19.2px;color:#444}
.col-testimonial .copy{top:101px;left:40px;right:40px;font-size:13px;line-height:22.5px}
.btn{position:absolute;left:50%;transform:translateX(-50%);background:var(--red);color:#fff;font-size:10.5px;height:21px;line-height:21px;padding:0 9px;white-space:nowrap}
.avatar{position:absolute;left:176px;top:195px;width:45px;height:45px;border-radius:50%;background:linear-gradient(180deg,#7a7d80,#c5c5c5)}
.signup{position:absolute;left:44px;top:136px;width:318px;height:46px;border:1px solid #d0d0d0;background:#fff}
.signup .field{position:absolute;left:12px;top:15px;font-size:11.5px;color:#555;display:flex;gap:10px;align-items:center}
.signup .go{position:absolute;right:6px;top:6px;width:90px;height:33px;background:var(--red);color:#fff;font-weight:500;font-size:13px;line-height:33px;text-align:center;letter-spacing:.3px}
.col-updates .note{position:absolute;left:0;width:100%;top:242px;font-size:12.5px;line-height:21px;color:#444}

/* footer */
.site-footer{position:absolute;left:0;top:886px;width:1200px;height:66px;background:var(--footer);color:#ddd;font-size:11px;text-align:center;line-height:66px;word-spacing:1px}
.site-footer span{margin:0 8px;color:#aaa}
</style>
</head>
<body>

<header class="site-header">
  <div class="brand">GAPWISE360</div>
  <nav class="nav"><a class="active" href="#">Medicare Supplement</a></nav>
  <span class="nav-item" style="left:370px">Part D</span>
  <span class="nav-item" style="left:440px">How To Decide</span>
  <span class="nav-item" style="left:565px">Learn Online</span>
  <span class="nav-item" style="left:674px">Why Gapwise 360</span>
  <span class="nav-item" style="left:811px">Buy Now</span>
  <div class="divider" style="left:882px"></div>
  <div class="rates">
    <div class="label">Compare Rates and Save</div>
    <div class="phone">(800) 555 - 0142</div>
  </div>
  <div class="divider" style="left:1052px"></div>
  <div class="connect">
    <div class="label">Connect with us</div>
    <div class="socials">
      <span style="background:#3b5998"></span>
      <span style="background:#1da1f2"></span>
      <span style="background:#e25b45"></span>
      <span style="background:#e52d27"></span>
    </div>
  </div>
</header>

<section class="hero-photo" role="img" aria-label="Businessman working on a laptop in an office chair beside a city-view window"></section>
<div class="why-box">
  <h1>WHY US?</h1>
  <p>Contrary to popular belief, Lorem Ipsum is not simply random text. It has roots in a piece of classical</p>
</div>

<section class="hero-video" role="img" aria-label="Video still of a smiling young man with glasses at a computer">
  <svg class="play" width="78" height="78" viewBox="0 0 78 78">
    <circle cx="39" cy="39" r="35" fill="none" stroke="#fff" stroke-width="6" opacity=".9"/>
    <path d="M30 22 L56 39 L30 56 Z" fill="#fff" opacity=".9"/>
  </svg>
  <div class="video-bar">
    <div class="progress"><i></i></div>
    <svg style="position:absolute;left:8px;top:8px" width="10" height="11"><rect x="1" y="1" width="3" height="9" fill="#fff"/><rect x="6" y="1" width="3" height="9" fill="#fff"/></svg>
    <span class="time">04:29 | 02:47</span>
    <svg style="position:absolute;left:362px;top:9px" width="58" height="10"><rect x="0" y="2" width="16" height="6" fill="#fff"/><rect x="18" y="0" width="4" height="10" fill="#fff"/><rect x="24" y="4" width="30" height="2" fill="#555"/></svg>
    <svg style="position:absolute;left:440px;top:7px" width="12" height="12"><path d="M1 11 L11 1 M5 1 H11 V7" stroke="#fff" stroke-width="2" fill="none"/></svg>
  </div>
</section>

<section class="features">
  <div class="feature f1">
    <svg width="38" height="34" viewBox="0 0 38 34" fill="none" stroke="#fff" stroke-width="2.5"><path d="M19 3 V10 M6 8 H32"/><path d="M2 22 L9 9 L16 22 Z" fill="#fff"/><path d="M22 26 L29 12 L36 26 Z" fill="#fff"/><circle cx="19" cy="5" r="3"/></svg>
    <span>Compare <b>Rated</b></span>
  </div>
  <div class="feature f2">
    <svg width="36" height="32" viewBox="0 0 36 32" fill="none" stroke="#fff" stroke-width="2.5"><path d="M1 3 H7 L11 22 H30 L34 8 H9"/><path d="M12 13 H32 M11 17 H31"/><circle cx="14" cy="28" r="2.5" fill="#fff"/><circle cx="27" cy="28" r="2.5" fill="#fff"/></svg>
    <span>Buy <b>Now</b></span>
  </div>
  <div class="feature f3">
    <svg width="28" height="28" viewBox="0 0 28 28"><circle cx="14" cy="14" r="13" fill="#fff"/><path d="M8 6 C12 8 12 12 9 14 C7 16 10 19 12 20 M18 5 C16 8 19 10 21 10 M20 16 C18 18 19 22 21 23" stroke="var(--navy-3)" stroke-width="3" fill="none"/></svg>
    <span>Learn <b>Online</b></span>
  </div>
  <div class="feature f4">
    <svg width="48" height="36" viewBox="0 0 48 36" fill="none" stroke="#fff" stroke-width="2.2"><path d="M14 2 H46 V20 H40 V26 L34 20 H28"/><path d="M2 10 H30 V28 H14 L8 34 V28 H2 Z"/><circle cx="9" cy="19" r="1.5" fill="#fff"/><circle cx="16" cy="19" r="1.5" fill="#fff"/><circle cx="23" cy="19" r="1.5" fill="#fff"/></svg>
    <span>Get Expert <b>Help</b></span>
  </div>
</section>

<main class="content">
  <section class="col col-welcome">
    <div class="kicker">GAPWISE360</div>
    <h2><b>Welcome</b> to our site</h2>
    <div class="rule"></div>
    <p class="copy">Sed ut perspiciatis unde omnis iste natus error sit voluptatem accusantium doloremque laudantium, totam rem aperiam, eaque ipsa quae ab illo inventore veritatis et quasi architecto beatae vitae dicta sunt explicabo Nemo enim ipsam voluptatem quia voluptas sit aspernatur aut odit aut fugit, sed quia consequuntur magni dolores eos</p>
    <span class="btn" style="top:254px">READ MORE</span>
  </section>

  <section class="col col-testimonial">
    <h2><b>What People</b> are saying</h2>
    <div class="rule"></div>
    <p class="copy">I had a grest experience but bewareof the Gapwise360 IT Team. You never know what you are going get. And thats all I have to say about that</p>
    <div class="avatar" role="img" aria-label="Portrait of the reviewer"></div>
    <span class="btn" style="top:254px">Marla Quinn</span>
  </section>

  <section class="col col-updates">
    <h2><b>Monthly</b> Updates</h2>
    <div class="rule"></div>
    <div class="signup">
      <div class="field">
        <svg width="13" height="10" viewBox="0 0 13 10"><rect width="13" height="10" fill="#555"/><path d="M0 0 L6.5 5 L13 0" stroke="#fff" stroke-width="1.2" fill="none"/></svg>
        <span>E mail Id</span>
      </div>
      <div class="go">SIGNUP!</div>
    </div>
    <p class="note">Enter Email for Customized Monthly Rate<br>Updates and More</p>
  </section>
</main>

<footer class="site-footer">
  Gapwise360<span>|</span>Sitemap<span>|</span>Buy Now<span>|</span>Blog<span>|</span>Login<span>|</span>Copyrights @ 2016 All Rights Reserved
</footer>

</body>
</html>
```